Business Card Design Project

I want a design for my business cards based on an excisting logo design.

Target Market(s)

Marketeers, PR-peeps, CEO's, decisionmakers, entrepreneurs

Industry/Entity Type

Business

Requirements
Nice to have
• Some visual interest on the back too
Should not have
• Sarif on the font

```html
<!DOCTYPE html>
<html lang="nl">
<head>
<meta charset="utf-8">
<title>FernPeakPR – visitekaartje</title>
<link rel="stylesheet" href="https://fonts.googleapis.com/css2?family=Cinzel:wght@600&family=Open+Sans:ital,wght@0,400;0,700;1,700&display=swap">
<style>
  :root {
    --backdrop: #d9d9d9;
    --card-white: #ffffff;
    --card-black: #141211;
    --card-black-glow: #2c2826;
    --ink: #3a3a3a;
    --brand-grey: #8a8a8c;
    --band-grey: #7b7b7d;
    --brand-green: #0e9a45;
    --leaf-green: #9cc93a;
    --white: #ffffff;
  }
  * { box-sizing: border-box; margin: 0; padding: 0; }
  html, body { width: 971px; height: 1200px; overflow: hidden; }
  body {
    position: relative;
    background: var(--backdrop);
    font-family: "Open Sans", Arial, sans-serif;
    color: var(--ink);
  }
  .card {
    position: absolute;
    left: 80px;
    width: 800px;
    height: 457px;
    border-radius: 26px;
    overflow: hidden;
    box-shadow: 0 4px 10px rgba(0,0,0,0.35);
  }
  /* front */
  .card--front { top: 103px; background: var(--card-white); }
  .tagline {
    position: absolute; top: 45px; left: 0; width: 100%;
    text-align: center;
    font-family: "Cinzel", Georgia, serif;
    font-weight: 600; font-size: 17px; line-height: 22px;
    color: var(--ink); letter-spacing: 0.5px;
  }
  .brand {
    position: absolute; top: 94px; left: 43px;
    display: flex; align-items: center; gap: 36px;
  }
  .brand__dot {
    width: 116px; height: 116px; border-radius: 50%;
    background: var(--leaf-green);
  }
  .brand__name {
    font-size: 76px; font-weight: 400; color: var(--brand-grey);
    letter-spacing: 2px; line-height: 1;
  }
  .person {
    position: absolute; top: 222px; left: 0; width: 100%;
    text-align: center; font-weight: 700; font-size: 24px; color: var(--ink);
  }
  .contact {
    position: absolute; top: 270px; left: 0; width: 100%;
    text-align: center; font-size: 18px; line-height: 30px; color: var(--ink);
  }
  .contact b { font-style: italic; font-weight: 700; }
  .front-base { position: absolute; left: 0; top: 367px; width: 800px; height: 90px; }
  .address {
    position: absolute; bottom: 12px; left: 0; width: 100%;
    text-align: center; font-size: 25px; color: var(--white);
  }
  /* back */
  .card--back {
    top: 635px;
    background: radial-gradient(ellipse at 50% 40%, var(--card-black-glow) 0%, var(--card-black) 70%);
  }
  .back-dot {
    position: absolute; left: 288px; top: 43px;
    width: 230px; height: 230px; border-radius: 50%;
    background: var(--leaf-green);
  }
  .back-name {
    position: absolute; top: 292px; left: 0; width: 100%;
    text-align: center; font-size: 50px; color: var(--brand-grey);
    letter-spacing: 1px;
  }
  .back-url {
    position: absolute; top: 398px; left: 0; width: 100%;
    text-align: center; font-size: 27px; color: var(--white);
  }
</style>
</head>
<body>
  <section class="card card--front">
    <p class="tagline">SYSTEMISCH EN STRATEGISCH PR-<br>MARKETING- EN COMMUNICATIEADVIES</p>
    <div class="brand">
      <span class="brand__dot"></span>
      <span class="brand__name">FernPeakPR</span>
    </div>
    <p class="person">Mara Linden</p>
    <p class="contact">
      <b>p</b> : +31(0)6 12345678 &nbsp;|&nbsp; <b>e</b> : mara.linden@fernpeakpr.nl<br>
      <b>w</b> : www.fernpeakpr.nl<br>
      <b>t</b> : social.example/_fernpeakpr &nbsp;|&nbsp; <b>f</b> : friends.example/fernpeakpr
    </p>
    <svg class="front-base" viewBox="0 0 800 90" aria-hidden="true">
      <path d="M0,28 Q400,-12 800,28 L800,36 Q400,-4 0,36 Z" fill="var(--band-grey)"/>
      <path d="M0,44 Q400,16 800,44 L800,90 L0,90 Z" fill="var(--brand-green)"/>
    </svg>
    <p class="address">Lindelaan 42, 6701 AB Groenveld</p>
  </section>

  <section class="card card--back">
    <span class="back-dot"></span>
    <p class="back-name">FernPeakPR</p>
    <p class="back-url">www.fernpeakpr.nl</p>
  </section>
</body>
</html>
```